Stationery Design Project - New innovative law firm

I need a simple design, yet the tone of the stationery set need to express modern, professionalism, smart and forward-thinking. I don’t need a business card, but require the stationery set to have:
• Design letterhead
• Design facsimile
• Design memo
The triangular logo with Halvard Lane words etc, need to be present in the stationery. The red triangular logo should not be re-designed, but feel free to play around with the placement and colours of the Halvard Lane words etc....?

Target Market(s)

Business clients

Industry/Entity Type

Business

Requirements
Must have
• The triangular logo with Halvard Lane words etc...for branding.

```html
<!DOCTYPE html>
<html lang="en">
<head>
<meta charset="utf-8">
<title>Halvard Lane Letterhead</title>
<link href="https://fonts.googleapis.com/css2?family=Arimo:wght@400;700&display=swap" rel="stylesheet">
<style>
  :root {
    --brand-red: #e31e24;
    --ink: #3a3a3a;
    --ink-soft: #6b6b6b;
    --band-dark: #2b2b2b;
    --paper: #ffffff;
    --backdrop-light: #d6d6d6;
    --backdrop-dark: #a9a9a9;
  }
  * { margin: 0; padding: 0; box-sizing: border-box; }
  html, body { width: 1200px; height: 900px; overflow: hidden; }
  body {
    background: radial-gradient(ellipse at center, var(--backdrop-light) 0%, var(--backdrop-dark) 100%);
    font-family: "Arimo", Arial, sans-serif;
    color: var(--ink);
    position: relative;
  }
  .letterhead {
    position: absolute;
    left: 300px; top: 26px;
    width: 600px; height: 848px;
    background: var(--paper);
    box-shadow: 0 4px 18px rgba(0,0,0,.25);
  }
  .brand { position: absolute; left: 58px; top: 62px; display: flex; align-items: center; gap: 10px; }
  .brand-square { width: 34px; height: 34px; background: var(--brand-red); }
  .brand-name { font-size: 22px; font-weight: 700; color: var(--ink); letter-spacing: .5px; line-height: 1; text-transform: uppercase; }
  .brand-tagline { font-size: 7.5px; font-weight: 700; color: var(--ink-soft); text-transform: uppercase; margin-top: 3px; letter-spacing: .2px; }
  .reference { position: absolute; right: 58px; top: 132px; font-size: 8px; color: var(--ink); }
  .letter-date { position: absolute; left: 58px; top: 164px; font-size: 8px; color: var(--ink-soft); }
  .recipient { position: absolute; left: 58px; top: 190px; font-size: 8px; line-height: 11px; color: var(--ink-soft); }
  .recipient-name { font-size: 10px; font-weight: 700; color: var(--ink); margin-bottom: 1px; }
  .recipient-company { color: var(--ink); }
  .letter-body {
    position: absolute; left: 58px; right: 58px; top: 290px;
    font-size: 9.6px; line-height: 14px; text-align: justify; color: var(--ink);
  }
  .letter-body p { text-indent: 14px; }
  .sign-off { position: absolute; left: 72px; top: 620px; font-size: 9.6px; }
  .signature {
    position: absolute; left: 80px; top: 640px; width: 110px; height: 56px;
    background: linear-gradient(90deg, rgba(60,60,60,.08), rgba(60,60,60,.18), rgba(60,60,60,.06));
    border-radius: 4px;
  }
  .signatory { position: absolute; left: 72px; top: 706px; font-size: 9.6px; line-height: 13px; }
  .signatory-name { font-weight: 700; font-size: 10.5px; }
  .signatory-email { font-size: 8px; color: var(--ink-soft); }
  .office-contact { position: absolute; right: 58px; top: 706px; text-align: right; font-size: 8px; line-height: 11px; color: var(--ink-soft); }
  .office-contact .label { color: var(--brand-red); }
  .office-contact .gap { margin-top: 8px; }
  .footer-band { position: absolute; left: 0; bottom: 0; width: 600px; height: 34px; }
  .web-address {
    position: absolute; right: 58px; bottom: 12px;
    color: #fff; font-size: 10px;
  }
  .web-address b { font-weight: 700; }
</style>
</head>
<body>
  <main class="letterhead">
    <header class="brand">
      <div class="brand-square"></div>
      <div>
        <div class="brand-name">Halvard Lane</div>
        <div class="brand-tagline">Accounting, Tax, Business Advice &amp; Legal</div>
      </div>
    </header>

    <div class="reference">Ref: 452735AD/2</div>
    <div class="letter-date">March 04, 2011</div>

    <address class="recipient" style="font-style:normal">
      <div class="recipient-name">Mr Owen Marsh</div>
      <div>Managing Director</div>
      <div class="recipient-company">Northgate Holdings</div>
      <div>240 Cedar Avenue</div>
      <div>Brookfield, WA 98601</div>
    </address>

    <section class="letter-body">
      <p>Dolorpor re nobitibus. Et ation pa dolorerro volupta quiam, sequas escia seque magnim et etum fugitatio. Acepudis del moluptatquo eiur? Qui nis estiam, sit earci omnisita qui iliquam dolenes experestor sit milles acidunto quas nos erum, ipid utem quia cum dist repella verionseque voluptaque vellaut que perferum ullati dolorendi im exercil litetur?</p>
      <p>Em digentis arum acerumquo et ad ulparum esendam volorestio. Ebit fuga. Nam et lique doloris moluptatum illes verferchil molorro vellit quo que doluptas auta non rerum atiate volor aut liqui te coneturis aliquam nobitempore pos mo bla nonsequae sinimperum nimet ma sandis poreperum ad maxim dolupta tquossit pa coriberia volupta tioris eveliamus, autet ma dignis istium dolupta num quis dionseque laccumque id maximpel ium aditatur se eostrum voles et estibus.</p>
      <p>Ibusandant que nos ex experum quae. Met laccusci ventiam, quid eument ommolor ibust, qui qui volorpores si beari ut doluptatur, omnime erspero vellore rnatiisitis unto berio. Verferit endipit mos earum nimus doluptam, odipsandici nus es nulluptiati cum volum re et andi omnimagnimet dipit maio. Osandunt mi, ium vendaer iberum ut aut fugia earum quis sereicte voluptusanti autassi aruptatem quatium eliciur sinulluptati blabo. Nequi comniscid quamusc ienihil ma dolor magnat ligenis est unt hic tem quatinc ientet qui officit et velis ute latus rescien ihillit eic tectatiam int harunto corepel laccumquamus et dollace ssincit endant audanto molestios que nempori doloria nisquosam ius reheni con porent, versper naturit et ipsam acere, que qui que nihiliq uidunt inverio es possit, cum sum eos dolorem nit omnis enem arum aut lam, consequ aestin non perro inctur?</p>
    </section>

    <div class="sign-off">Yours faithfully</div>
    <div class="signature" role="img" aria-label="Handwritten signature of the signatory"></div>

    <div class="signatory">
      <div class="signatory-name">Mara Quinlan</div>
      <div>Managing Partner</div>
      <div class="signatory-email">mara.quinlan@halvardlane.com.au</div>
    </div>

    <address class="office-contact" style="font-style:normal">
      <div class="label">Adress:</div>
      <div>Suite 4/18 Alder St,</div>
      <div>Ridgeford, NSW 2190</div>
      <div class="gap"><span class="label">Ph:</span>+61 2 9000 4821</div>
      <div><span class="label">Mob:</span>+61 400 000 372</div>
      <div class="gap"><span class="label">E:</span>admin@halvardlane-advisory.com.au</div>
    </address>

    <svg class="footer-band" viewBox="0 0 600 34" preserveAspectRatio="none" aria-hidden="true">
      <polygon points="0,14 400,14 390,34 0,34" fill="var(--band-dark)"/>
      <polygon points="412,4 600,4 600,34 400,34" fill="var(--brand-red)"/>
    </svg>
    <div class="web-address">www.<b>halvardlane</b>.com.au</div>
  </main>
</body>
</html>
```